Brimwell is a steel frame construction company that builds residential and commercial homes

1. Homepage (we are after a basic website)
Hero Section:
A full-width image or video showcasing steel frames in construction or a finished project.
Tagline: Short, impactful tagline (e.g., "Strong Structures for Tomorrow").
Call-to-Action (CTA): A prominent "Get a Quote" or "Contact Us" button.
About Us (Snapshot Section):

A few lines about the company, emphasizing experience, certifications, and commitment to quality.
Include a "Learn More" button linking to the detailed About Us page.
Products/Services Section:

Feature the main products like steel frames for industrial, residential, and commercial projects.
Each category should have a "Learn More" link to a dedicated product page.
Project Showcase/Portfolio:

Display 2-3 featured projects with images, descriptions, and a "View All Projects" button.
Certifications & Partners:

Display logos of certifications (ISO, local building standards) and partnerships with construction companies or industry bodies.
Footer:

Contact information, quick links (Home, About, Products, Services, Contact), and social media icons.
2. Products Page
Overview:

A grid or list layout showing different steel frame products or services.
Each product should have a title, brief description, and a thumbnail image.
Individual Product Pages:

Detailed information on specific products (e.g., “Steel Frames for Residential Construction”):
Features: Highlight specific features like durability, eco-friendliness, precision, etc.
Technical Specs: Material grades, dimensions, finishes available.
Case Studies: A couple of client testimonials or case studies of where this product was used.
Downloadable Resources:

Technical datasheets or catalogs for users to download.
Include a form to capture user information before they download the document (optional for lead generation).
3. Projects/Portfolio Page
Gallery of Projects:
Display completed projects with high-quality images, each linked to a project detail page.
Filter options (e.g., industrial, residential, commercial).
Project Detail Pages:
A detailed description of the project, challenges, and how the steel frames were used.
other website we liked are:
https://www.brimwellframing.com.au/
https://quorvantframe.com.au/

1. Objective:
Create an informative, professional, and visually appealing website that promotes steel frame construction solutions, showcasing the company’s offerings, expertise, and projects.
The website should highlight the benefits of steel frames (e.g., durability, sustainability, and cost-efficiency) and cater to both B2B and B2C clients.
2. Target Audience:
Primary: Architects, builders, and construction companies.
Secondary: Homeowners, investors, and property developers looking for modern, durable construction solutions.

```html
<!DOCTYPE html>
<html lang="en">
<head>
<meta charset="utf-8">
<title>Brimwell — Steel Frame Construction</title>
<link href="https://fonts.googleapis.com/css2?family=Montserrat:wght@400;500;600;700&display=swap" rel="stylesheet">
<style>
:root{
  --blue:#0a6fbd;
  --navy:#1f2a36;
  --ink:#1d2733;
  --muted:#555d66;
  --card:#e9eaec;
  --white:#ffffff;
  --dot:#8a9096;
}
*{box-sizing:border-box;margin:0;padding:0}
html,body{width:1200px;height:3028px;overflow:hidden}
body{font-family:'Montserrat',sans-serif;color:var(--ink);background:var(--white);position:relative}
.abs{position:absolute}
a{color:inherit;text-decoration:none}
.btn{position:absolute;background:var(--blue);color:var(--white);font-weight:600;font-size:15px;display:flex;align-items:center;justify-content:center}
.topbar{left:0;top:0;width:1200px;height:42px;background:var(--navy);color:var(--white);font-size:13px;font-weight:500}
.topbar .item{position:absolute;top:13px;display:flex;align-items:center;gap:8px}
.topbar .social{position:absolute;top:12px;width:16px;height:16px;border-radius:50%;background:var(--white)}
.nav{left:0;top:42px;width:1200px;height:84px;background:var(--white)}
.brand{position:absolute;display:flex;align-items:center;gap:8px;font-weight:700;color:var(--blue)}
.brand .mark{background:var(--blue)}
.nav .links a{position:absolute;top:33px;font-size:15px;font-weight:500;color:var(--ink)}
.hero{left:0;top:126px;width:1200px;height:604px;background:linear-gradient(135deg,#5a6068 0%,#3c4249 45%,#2e3339 70%,#4c525a 100%)}
.hero h1{position:absolute;left:0;width:1200px;top:228px;text-align:center;color:var(--white);font-size:46px;font-weight:600;line-height:50px}
.hero p{position:absolute;left:380px;width:440px;top:344px;text-align:center;color:var(--white);font-size:13px;line-height:20px}
.sec-title{position:absolute;font-size:32px;font-weight:700;color:var(--ink);text-align:center}
.rule{position:absolute;height:3px;width:76px;background:var(--blue)}
.card{position:absolute;top:965px;left:89px;width:324px;height:255px;background:var(--card);text-align:center}
.card.active{background:var(--blue);color:var(--white)}
.card h3{position:absolute;top:116px;left:0;width:100%;font-size:18px;font-weight:700;white-space:nowrap}
.card p{position:absolute;top:142px;left:28px;right:28px;font-size:13px;line-height:20px;color:var(--muted)}
.card.active p{color:var(--white);font-weight:500}
.card .more{position:absolute;top:217px;left:0;width:100%;font-size:14px;font-weight:600}
.card svg.icon{position:absolute;top:22px;left:127px}
.dots{position:absolute;display:flex;gap:6px}
.dots span{width:11px;height:11px;border-radius:50%;background:var(--dot)}
.dots span.on{background:var(--blue)}
.about-img{left:129px;top:1357px;width:484px;height:367px;border:2px solid #333;background:linear-gradient(135deg,#2f7fc0 0%,#1b5f9c 45%,#b9955f 80%,#3a79b3 100%)}
.about-text{left:644px;top:1528px;width:430px;font-size:13px;line-height:19.6px;color:var(--muted)}
.project{position:absolute;top:1889px;height:187px}
.project span{position:absolute;bottom:20px;color:var(--white);font-weight:700;font-size:18px}
.footer{left:0;top:2683px;width:1200px;height:345px;background:var(--navy);color:var(--white)}
.footer h4{position:absolute;font-size:23px;font-weight:700}
.footer ul{position:absolute;list-style:none;font-size:13px;font-weight:500}
.footer ul li{height:27px}
.footer .crow{position:absolute;display:flex;align-items:center;gap:10px;font-size:13px;font-weight:500}
.badge{position:absolute;top:2442px}
</style>
</head>
<body>

<header class="abs topbar">
  <div class="item" style="left:88px"><svg width="16" height="16" viewBox="0 0 24 24" fill="#fff"><path d="M6.6 10.8a15 15 0 0 0 6.6 6.6l2.2-2.2a1 1 0 0 1 1-.25 11.4 11.4 0 0 0 3.6.57 1 1 0 0 1 1 1V20a1 1 0 0 1-1 1A17 17 0 0 1 3 4a1 1 0 0 1 1-1h3.5a1 1 0 0 1 1 1c0 1.25.2 2.45.57 3.57a1 1 0 0 1-.25 1z"/></svg>+08 321 654 987</div>
  <div class="item" style="left:285px"><svg width="17" height="13" viewBox="0 0 24 18" fill="#fff"><path d="M0 0h24v18H0z M2 2l10 8 10-8" stroke="#1f2a36" stroke-width="2"/></svg>info@example.com</div>
  <div class="item" style="left:506px"><svg width="13" height="17" viewBox="0 0 24 32" fill="#fff"><path d="M12 0a12 12 0 0 0-12 12c0 9 12 20 12 20s12-11 12-20A12 12 0 0 0 12 0zm0 17a5 5 0 1 1 0-10 5 5 0 0 1 0 10z"/></svg>48 Forgeline Road, Unit 2</div>
  <span class="social" style="left:936px"></span>
  <span class="social" style="left:984px"></span>
  <span class="social" style="left:1038px"></span>
  <span class="social" style="left:1093px"></span>
</header>

<nav class="abs nav">
  <div class="brand" style="left:88px;top:24px;font-size:30px"><span class="mark" style="width:26px;height:26px"></span>Brimwell</div>
  <div class="links">
    <a style="left:563px">Home</a>
    <a style="left:646px">About Us</a>
    <a style="left:753px">Services</a>
    <a style="left:853px">Projects</a>
  </div>
  <a class="btn" style="left:963px;top:21px;width:147px;height:42px">Contact Us</a>
</nav>

<section class="abs hero" role="img" aria-label="Glass and steel office tower facade viewed from below">
  <h1>STRONG STRUCTURES FOR<br>TOMORROW</h1>
  <p>Strong Structures for Tomorrow Your reliable partner in steel frame construction.</p>
  <a class="btn" style="left:526px;top:402px;width:149px;height:40px">Get a Quote</a>
</section>

<h2 class="sec-title" style="left:0;width:1200px;top:884px">OUR SERVICES</h2>
<div class="rule" style="left:562px;top:936px"></div>

<article class="card" style="left:89px">
  <svg class="icon" width="70" height="72" viewBox="0 0 70 72" fill="none" stroke="#0a6fbd" stroke-width="2.5"><path d="M3 70V38l16-8v8l16-8v8h10V8h6v30h4V16h6v54z"/><path d="M12 48h6v6h-6zM28 48h6v6h-6zM44 48h6v6h-6zM28 60h8v10h-8z"/></svg>
  <h3>INDUSTRIAL STEEL FRAMES</h3>
  <p>Steel frames tailored for large-scale industrial applications, offering durability and efficiency.</p>
  <a class="more">Learn More →</a>
</article>
<article class="card active" style="left:437px">
  <svg class="icon" width="70" height="72" viewBox="0 0 70 72" fill="none" stroke="#fff" stroke-width="2.5"><path d="M4 34L35 6l31 28M12 28v42h46V28"/><path d="M24 70V46h12v24M42 44h12v12H42zM48 44v12M42 50h12"/></svg>
  <h3>RESIDENTIAL STEEL FRAMES</h3>
  <p>Custom steel framing solutions for homes, designed for strength, style, and safety.</p>
  <a class="more">Learn More →</a>
</article>
<article class="card" style="left:785px">
  <svg class="icon" width="74" height="72" viewBox="0 0 74 72" fill="none" stroke="#0a6fbd" stroke-width="2.5"><path d="M4 70V22h16v48M20 70V4h24v66M44 70V28h24v42M2 70h70"/><path d="M26 14h12M26 24h12M26 34h12M26 44h12M50 38h12M50 48h12M50 58h12M8 32h8M8 42h8M8 52h8"/></svg>
  <h3>COMMERCIAL STEEL FRAMES</h3>
  <p>Steel frames that offer structural integrity for office buildings, retail spaces, and more.</p>
  <a class="more">Learn More →</a>
</article>
<div class="dots" style="left:578px;top:1257px"><span></span><span class="on"></span><span></span></div>

<div class="abs about-img" role="img" aria-label="Blue steel wall and roof frames assembled on a construction site"></div>
<h2 class="sec-title" style="left:644px;top:1454px;text-align:left">ABOUT US BRIMWELL</h2>
<div class="rule" style="left:646px;top:1503px"></div>
<p class="abs about-text">At Brimwell, we bring years of experience, certified expertise, and an unwavering commitment to quality in every steel frame we build. Our dedication to creating robust and innovative structures for industrial, residential, and commercial projects sets us apart in the construction industry.</p>
<a class="btn" style="left:644px;top:1643px;width:149px;height:39px">Learn More</a>

<h2 class="sec-title" style="left:87px;top:1807px;text-align:left">PROJECT SHOWCASE</h2>
<div class="rule" style="left:89px;top:1857px"></div>
<p class="abs" style="left:658px;top:1810px;width:460px;font-size:13px;line-height:19.6px;color:var(--muted)">View highlights of our exceptional projects, demonstrating the versatility and strength of our steel frames.</p>

<div class="project" style="left:0;width:400px;background:linear-gradient(160deg,#9a9a9a 0%,#3a3a3a 55%,#151515 100%)" role="img" aria-label="Black and white steel framework of an industrial facility"><span style="left:106px">INDUSTRIAL FACILITY</span></div>
<div class="project" style="left:400px;width:402px;background:linear-gradient(180deg,#6e9fce 0%,#4b7eb0 55%,#2e5f93 100%)" role="img" aria-label="Residential building under construction with crane"><span style="left:16px;bottom:18px">RESIDENTIAL DEVELOPMENT</span></div>
<div class="project" style="left:802px;width:398px;background:linear-gradient(180deg,#8c8c8c 0%,#4a4a4a 60%,#0e0e0e 100%)" role="img" aria-label="Steel roof trusses of a commercial complex"><span style="left:17px;bottom:18px">COMMERCIAL COMPLEX</span></div>

<a class="btn" style="left:511px;top:2109px;width:178px;height:39px">View All Projects</a>

<h2 class="sec-title" style="left:0;width:1200px;top:2303px">CERTIFICATIONS &amp; PARTNERS</h2>
<div class="rule" style="left:562px;top:2354px"></div>
<p class="abs" style="left:200px;width:800px;top:2374px;text-align:center;font-size:13px;line-height:19.6px;color:var(--muted)">We are accredited by renowned industry bodies and collaborate with key players in the construction sector. Our certifications and partnerships underline our dedication to delivering high-quality and compliant solutions.</p>
<svg class="badge" style="left:357px" width="112" height="112" viewBox="0 0 112 112"><circle cx="56" cy="56" r="54" fill="none" stroke="#1f4f9a" stroke-width="3"/><circle cx="56" cy="56" r="36" fill="#1f4f9a"/></svg>
<svg class="badge" style="left:516px;top:2452px" width="166" height="96" viewBox="0 0 166 96"><rect x="16" y="2" width="148" height="58" rx="4" fill="none" stroke="#1f4f9a" stroke-width="3"/><rect x="60" y="72" width="46" height="14" fill="#1f4f9a"/></svg>
<svg class="badge" style="left:742px" width="114" height="114" viewBox="0 0 114 114"><circle cx="57" cy="46" r="44" fill="#1b57b0"/><rect x="4" y="96" width="106" height="14" fill="#1b57b0"/></svg>
<div class="dots" style="left:578px;top:2584px"><span></span><span class="on"></span><span></span></div>

<footer class="abs footer">
  <div class="brand" style="left:88px;top:126px;font-size:38px;color:#fff"><span class="mark" style="width:34px;height:34px;background:var(--blue)"></span>Brimwell</div>
  <h4 style="left:425px;top:60px">QUICK LINK</h4>
  <ul style="left:425px;top:98px"><li>Home</li><li>About</li><li>Testimonials</li><li>Projects</li><li>Services</li><li>Contact us</li></ul>
  <h4 style="left:658px;top:61px">CONTACT US</h4>
  <div class="crow" style="left:658px;top:100px"><svg width="11" height="14" viewBox="0 0 24 32" fill="#fff"><path d="M12 0a12 12 0 0 0-12 12c0 9 12 20 12 20s12-11 12-20A12 12 0 0 0 12 0zm0 17a5 5 0 1 1 0-10 5 5 0 0 1 0 10z"/></svg>48 Forgeline Road, City, State, ZIP</div>
  <div class="crow" style="left:658px;top:129px"><svg width="12" height="10" viewBox="0 0 24 18" fill="#fff"><path d="M0 0h24v18H0z"/></svg>info@brimwellframes.com</div>
  <div class="crow" style="left:658px;top:159px"><svg width="12" height="12" viewBox="0 0 24 24" fill="#fff"><path d="M6.6 10.8a15 15 0 0 0 6.6 6.6l2.2-2.2a1 1 0 0 1 1-.25 11.4 11.4 0 0 0 3.6.57 1 1 0 0 1 1 1V20a1 1 0 0 1-1 1A17 17 0 0 1 3 4a1 1 0 0 1 1-1h3.5a1 1 0 0 1 1 1c0 1.25.2 2.45.57 3.57a1 1 0 0 1-.25 1z"/></svg>(123) 555-0148</div>
  <h4 style="left:969px;top:61px">FOLLOW US</h4>
  <span class="abs" style="left:964px;top:103px;width:35px;height:35px;border-radius:50%;background:var(--blue)"></span>
  <span class="abs" style="left:1005px;top:103px;width:35px;height:35px;border-radius:50%;background:#56606b"></span>
  <span class="abs" style="left:1045px;top:103px;width:35px;height:35px;border-radius:50%;background:#56606b"></span>
  <div class="abs" style="left:82px;top:290px;width:1036px;height:1px;background:#3a4551"></div>
  <p class="abs" style="left:0;width:1200px;top:307px;text-align:center;font-size:12px;font-weight:500">© 2024 BRIMWELL</p>
  <svg class="abs" style="left:1130px;top:272px" width="42" height="38" viewBox="0 0 42 38"><path d="M21 2C10 2 2 9 2 17c0 5 3 9 7 11l-3 8 9-6c2 .5 4 .7 6 .7 11 0 19-7 19-14S32 2 21 2z" fill="#fff"/><circle cx="13" cy="17" r="2.5" fill="#1f2a36"/><circle cx="21" cy="17" r="2.5" fill="#1f2a36"/><circle cx="29" cy="17" r="2.5" fill="#1f2a36"/></svg>
</footer>

</body>
</html>
```